Street Sign Project - Attract Customers

We need a street sign designed to display out the front of the building. It design will need to be 1800mm wide x 900mm high. We need to show potential customers where we are inviting. Some of the attachments are for inspiration. The sign will be printed on a sheet of aluminum. if you have a good look at our web site which is www.pk-r.com.au you should get a good feeling about the company and what we do.

Target Market(s)

Construction companies, landscaping and civil earth moving companies who may drive past our business

Industry/Entity Type

Building

Font styles to use
Sans Serif

Colors
ffffff
3277b5
000000

Requirements
Must have
• Company logo must be the main focus point
• The number "54" on the sign to show street number (300mm high)
• phone number - (02) 9418 3065
• web address - www.pk-r.com.au
• I have loaded pictures i would like to see used in the sign
Nice to have
• Banner picture as attached
Should not have
• Bright colours. Please use our blue colour where possible

```html
<!DOCTYPE html>
<html lang="en">
<head>
<meta charset="utf-8">
<title>Portlock Kinetic Rigging – Street Sign</title>
<link rel="stylesheet" href="https://fonts.googleapis.com/css2?family=Oswald:wght@700&family=Montserrat:ital,wght@0,600;0,800;1,900&display=swap">
<style>
  :root {
    --black: #000000;
    --white: #ffffff;
    --brand-blue: #3277b5;
    --photo-sky: #9cc3e6;
    --photo-steel: #8a9099;
    --photo-roof: #c06a4a;
    --photo-rubble: #a89c8c;
    --photo-blue: #2f6fc0;
  }
  * { margin: 0; padding: 0; box-sizing: border-box; }
  html, body { width: 1200px; height: 600px; overflow: hidden; background: var(--white); }
  .sign { position: relative; width: 1200px; height: 600px; background: var(--white); overflow: hidden; }
  .sign__backdrop { position: absolute; inset: 0; width: 1200px; height: 600px; }
  .street-number {
    position: absolute; left: 0; top: 0; width: 118px; height: 102px;
  }
  .street-number__label {
    position: absolute; left: 0; top: -6px; width: 118px; text-align: center;
    font-family: "Oswald", sans-serif; font-weight: 700; font-size: 66px;
    color: var(--black); letter-spacing: -1px;
  }
  .contact { position: absolute; left: 0; width: 1200px; text-align: center; color: var(--white); }
  .contact__phone {
    top: 128px; font-family: "Montserrat", sans-serif; font-style: italic; font-weight: 900;
    font-size: 66px; letter-spacing: 1px;
  }
  .contact__web {
    top: 200px; font-family: "Montserrat", sans-serif; font-weight: 600; font-size: 40px;
  }
  .service-photo {
    position: absolute; width: 184px; height: 184px; border-radius: 50%;
    border: 3px solid var(--black); background: var(--white); padding: 6px;
  }
  .service-photo__fill { width: 100%; height: 100%; border-radius: 50%; }
  .service-photo--platform { left: 120px; top: 318px; }
  .service-photo--platform .service-photo__fill { background: linear-gradient(160deg, #e9ecef, var(--photo-steel) 70%, #c0502e); }
  .service-photo--hoist { left: 325px; top: 340px; }
  .service-photo--hoist .service-photo__fill { background: linear-gradient(170deg, #b9bcc0, var(--photo-blue) 75%, #5a6068); }
  .service-photo--roof { left: 535px; top: 320px; }
  .service-photo--roof .service-photo__fill { background: linear-gradient(160deg, var(--photo-sky) 30%, var(--photo-roof) 55%, #cfcfcf); }
  .service-photo--chute { left: 748px; top: 296px; }
  .service-photo--chute .service-photo__fill { background: linear-gradient(180deg, var(--photo-sky), var(--photo-blue) 50%, #b8b8b0); }
  .service-photo--rubble { left: 956px; top: 254px; }
  .service-photo--rubble .service-photo__fill { background: linear-gradient(180deg, #9a7a55 20%, #c8c4bc 45%, var(--photo-rubble)); }
  .brand {
    position: absolute; left: 930px; top: 470px; display: flex; align-items: center; gap: 12px;
  }
  .brand__mark { width: 22px; height: 22px; background: var(--brand-blue); flex: none; }
  .brand__name {
    font-family: "Montserrat", sans-serif; font-weight: 800; font-size: 27px; line-height: 1.12;
    color: var(--brand-blue); text-transform: uppercase;
  }
</style>
</head>
<body>
<main class="sign">
  <svg class="sign__backdrop" viewBox="0 0 1200 600" aria-hidden="true">
    <path class="sign__panel" fill="var(--black)"
      d="M0,0 H1200 V195 C1010,315 760,368 480,364 C300,360 130,345 0,328 Z"/>
    <path class="sign__swoosh" fill="var(--black)"
      d="M0,362 C160,388 340,400 500,398 C800,394 1010,320 1200,232 V268 C1010,372 800,440 500,446 C310,449 130,424 0,398 Z"/>
  </svg>

  <div class="street-number">
    <svg width="118" height="102" viewBox="0 0 118 102" aria-hidden="true">
      <path fill="var(--white)" d="M0,0 H118 V74 L59,102 L0,74 Z"/>
    </svg>
    <span class="street-number__label">54</span>
  </div>

  <p class="contact contact__phone">(02) 9418 3065</p>
  <p class="contact contact__web">www.pk-r.com.au</p>

  <div class="service-photo service-photo--platform"><div class="service-photo__fill" role="img" aria-label="Worker on a mast climbing work platform"></div></div>
  <div class="service-photo service-photo--hoist"><div class="service-photo__fill" role="img" aria-label="Blue construction hoist inside scaffolding"></div></div>
  <div class="service-photo service-photo--roof"><div class="service-photo__fill" role="img" aria-label="Inclined ladder hoist against a tiled roof"></div></div>
  <div class="service-photo service-photo--chute"><div class="service-photo__fill" role="img" aria-label="Blue rubbish chute down a building facade"></div></div>
  <div class="service-photo service-photo--rubble"><div class="service-photo__fill" role="img" aria-label="Conveyor belt over demolition rubble"></div></div>

  <div class="brand">
    <span class="brand__mark" aria-hidden="true"></span>
    <p class="brand__name">Portlock<br>Kinetic<br>Rigging</p>
  </div>
</main>
</body>
</html>
```